Brackenvale Herons Soccer Club/Duelmark Football Programs needs a flyer for promotions to young students

We are a soccer(football) club based in Melbourne(suburb of Campbellfield) and are running a professional 5 day a week all year round program for kids aged 8 to 18. Our target is to attract approximately 225 kids to our program by the 8th of march this year(4 weeks).
What sets our program apart is our message and mission statement:
- DuelmarkFootball Programs will send players for a European or local Professional trial when they are ready
- Train like a professional 5 days a week all year round
- Proven program over 12 years
- Testimonials on website http://www.brackenvaleherons-qx.com
The message on the flyer needs to be clear and concise.
"Come and try our program FREE for 3 days"
Lorne Habib,Harbourton Rovers 2015/2016 says "..............."
From only $10 a day
Milo Ferrand Reserve cnr Ashgrove and Tulloch Rd Brackenvale
Positions Limited, Register Now.....website..............
Call Rina Obu on 0400918372, Paul Vasko on 0400736154, Peter Stravinou on 0400482690
Example of a flyer uploaded. Can we magnify our message?

Target Market(s)

children and youth aged 8 years to 18 years

Industry/Entity Type

Club

Requirements
Must have
• at least one testimonial
• background image
• clear, concise with no clutter

```html
<!DOCTYPE html>
<html lang="en">
<head>
<meta charset="utf-8">
<title>Brackenvale Herons Soccer Club – Duelmark Football Programs</title>
<link rel="stylesheet" href="https://fonts.googleapis.com/css2?family=Exo+2:ital,wght@1,900&family=Archivo:ital,wght@0,700;0,800;1,800&family=Roboto:wght@300;400;700&display=swap">
<style>
  :root {
    --maroon: #6e1016;
    --orange: #e0521f;
    --sky-top: #5a1a22;
    --sky-mid: #c9401a;
    --stadium: #2a1a17;
    --pitch: #5f7a2c;
    --white: #ffffff;
    --ink: #111111;
    --silver-hi: #f4f4f4;
    --silver-lo: #8d8d8d;
  }
  * { margin: 0; padding: 0; box-sizing: border-box; }
  html, body { width: 849px; height: 1200px; overflow: hidden; background: #fff; }
  .flyer { position: relative; width: 849px; height: 1200px; overflow: hidden; font-family: "Archivo", sans-serif; }

  .backdrop {
    position: absolute; inset: 0;
    background:
      radial-gradient(ellipse 300px 480px at 170px 560px, rgba(190,40,30,.55), transparent 70%),
      linear-gradient(180deg, var(--sky-top) 0%, #8a2a1e 10%, var(--sky-mid) 22%, #d4561e 32%, #6a2a1c 40%, var(--stadium) 52%, #3a2a20 68%, #4d6426 74%, var(--pitch) 85%, #7c8f3a 100%);
  }

  .headline {
    position: absolute; left: 0; top: 22px; width: 849px; text-align: center;
    font-family: "Exo 2", sans-serif; font-style: italic; font-weight: 900;
    font-size: 68px; line-height: 58px; text-transform: uppercase; letter-spacing: 1px;
    background: linear-gradient(180deg, var(--silver-hi) 0%, #d0d0d0 45%, var(--silver-lo) 55%, #e6e6e6 100%);
    -webkit-background-clip: text; background-clip: text; color: transparent;
    filter: drop-shadow(2px 3px 2px rgba(0,0,0,.6));
  }

  .testimonial {
    position: absolute; left: 400px; top: 234px; width: 390px; text-align: center;
    color: var(--white); font-weight: 800; font-size: 27px; line-height: 35.5px;
    text-transform: uppercase; text-shadow: 1px 2px 3px rgba(0,0,0,.5);
  }
  .testimonial q { font-style: italic; display: block; quotes: "\"" "\""; }

  .club-card {
    position: absolute; left: 384px; top: 450px; width: 421px; height: 140px;
    background: var(--white); text-align: center; padding-top: 14px;
  }
  .club-card__name { color: var(--maroon); font-weight: 800; font-size: 32px; line-height: 38px; text-transform: uppercase; }
  .club-card__program { color: var(--ink); font-weight: 800; font-size: 27px; line-height: 40px; margin-top: 2px; }

  .venue {
    position: absolute; left: 384px; top: 590px; width: 421px; height: 163px;
    border: 2px solid var(--white); border-top: none; background: rgba(20,15,15,.55);
    color: var(--white); font-family: "Roboto", sans-serif; font-weight: 300;
    font-size: 24px; line-height: 30px; text-align: center; padding-top: 16px;
  }
  .venue__hours { margin-top: 12px; }

  .pitch-line {
    position: absolute; left: 375px; width: 440px; text-align: center; color: var(--white);
    font-weight: 800; font-style: italic; font-size: 20.5px; text-transform: uppercase;
    -webkit-text-stroke: 0.6px #222; text-shadow: 1px 1px 2px rgba(0,0,0,.7);
  }
  .divider { position: absolute; left: 405px; top: 832px; width: 395px; height: 2px; background: rgba(255,255,255,.8); }

  .offer { position: absolute; left: 375px; top: 838px; width: 460px; text-align: center; color: var(--white); font-weight: 800; text-shadow: 1px 2px 3px rgba(0,0,0,.5); }
  .offer__lead { font-size: 29px; line-height: 36px; }
  .offer__free { font-size: 39px; line-height: 42px; text-transform: uppercase; }

  .price { position: absolute; left: 30px; top: 800px; width: 160px; text-align: center; color: var(--white); font-family: "Roboto", sans-serif; text-shadow: 1px 2px 3px rgba(0,0,0,.45); }
  .price__from { font-weight: 300; font-size: 29px; line-height: 34px; }
  .price__amount { font-weight: 700; font-size: 80px; line-height: 78px; }
  .price__amount sup { font-size: 44px; vertical-align: 26px; }
  .price__unit { font-weight: 300; font-size: 40px; line-height: 44px; }

  .ball { position: absolute; left: 632px; top: 922px; width: 136px; height: 136px; border-radius: 50%; background: radial-gradient(circle at 40% 35%, #f4f4f4, #c9c9c9 70%, #9a9a9a); }

  .footer-band { position: absolute; left: 0; top: 1000px; width: 849px; height: 200px; }

  .club-mark { position: absolute; left: 18px; top: 990px; width: 190px; height: 190px; display: flex; flex-direction: column; align-items: center; justify-content: center; gap: 8px; }
  .club-mark__dot { width: 60px; height: 60px; border-radius: 50%; background: var(--orange); }
  .club-mark__name { color: var(--orange); font-weight: 800; font-size: 17px; line-height: 20px; text-align: center; text-transform: uppercase; }

  .contact { position: absolute; left: 225px; top: 1061px; width: 610px; text-align: center; font-weight: 800; }
  .contact__register { color: var(--maroon); font-size: 18px; line-height: 24px; }
  .contact__person { color: var(--ink); font-size: 19px; line-height: 25.5px; letter-spacing: .3px; }

  .disclaimer { position: absolute; left: 0; top: 1180px; width: 849px; text-align: center; font-family: "Roboto", sans-serif; font-size: 9.3px; color: var(--ink); }
</style>
</head>
<body>
<main class="flyer">
  <div class="backdrop" role="img" aria-label="Night stadium under an orange sky with a female footballer in red kit mid-kick across the left side"></div>

  <h1 class="headline">Make your soccer<br>dream a reality</h1>

  <blockquote class="testimonial">
    <q>I wouldn’t be here without you</q>
    <cite style="font-style:normal">Lorne Habib<br>Apex League, Harbourton Rovers Seniors 2015</cite>
  </blockquote>

  <section class="club-card">
    <h2 class="club-card__name">Brackenvale Herons<br>Soccer Club</h2>
    <p class="club-card__program">DuelmarkFootball Programs</p>
  </section>

  <address class="venue" style="font-style:normal">
    <p>Milo Ferrand Reserve,<br>cnr Ashgrove st and<br>Tulloch rds Brackenvale</p>
    <p class="venue__hours">5pm-7pm Monday to Friday</p>
  </address>

  <p class="pitch-line" style="top:765px">Train like the professionals</p>
  <p class="pitch-line" style="top:794px">5 days a week all year round</p>
  <div class="divider"></div>

  <div class="offer">
    <p class="offer__lead">Come and try our program</p>
    <p class="offer__free">Free for 3 days</p>
  </div>

  <div class="price">
    <p class="price__from">From only</p>
    <p class="price__amount"><sup>$</sup>10</p>
    <p class="price__unit">A DAY</p>
  </div>

  <div class="ball" role="img" aria-label="Football in flight"></div>

  <svg class="footer-band" viewBox="0 0 849 200" aria-hidden="true">
    <path d="M0 70 C 200 20, 500 40, 849 20 L849 200 L0 200 Z" fill="#b9b9b9"/>
    <path d="M0 78 C 200 28, 500 50, 849 30 L849 200 L0 200 Z" fill="#ffffff"/>
  </svg>

  <div class="club-mark">
    <span class="club-mark__dot"></span>
    <span class="club-mark__name">Brackenvale Herons</span>
  </div>

  <div class="contact">
    <p class="contact__register">Register now go to www.brackenvaleherons-qx.com or call</p>
    <p class="contact__person">Rina Obu 0400918372</p>
    <p class="contact__person">Paul Vasko 0400736154</p>
    <p class="contact__person">Peter Stravinou 0400482690</p>
  </div>

  <p class="disclaimer">Disclaimer: only players that have completed the DuelmarkFootball Program and deemed “ready”, “complete” by the coaching director will be eligible for European and local professional trials</p>
</main>
</body>
</html>
```